This is for a poster that will be hanging in the window of a Men's Suit Store in the mall:
Size 4 feet wide by 6 feet high
Main point is: A sale on "Suits" or "Men's Suits" at 40%-60% off ( the 40%-60% off should be the focal point)
Some words that can be used are "Sale" or "Clearance Sale"
Some key words that can be used to make it urgent are "limited time offer" or something similar.
You can get creative, the point is for the customer to want to come into the store and buy a suit right away.
You may use a graphic (picture of a man in a suit). It is not necessary but if it looks good you can use it. (If you do use a picture, it should be of a modern fit or slim fit suit)
Sorry, the initial brief somehow got deleted from the project. Please see the updated brief.
Thanks
Reason: Project was closed for some reason, extended to give enough time to complete
Target Market(s)
Mostly Men ages 35-55
Industry/Entity Type
Store
Colors
Designer to choose colors to be used in the design.

```html
<!DOCTYPE html>
<html lang="en">
<head>
<meta charset="utf-8">
<title>Men's Suits Clearance Sale Poster</title>
<link href="https://fonts.googleapis.com/css2?family=Poiret+One&family=Oswald:wght@700&display=swap" rel="stylesheet">
<style>
  :root {
    --canvas-bg: #e6e6e6;
    --poster-border: #ffffff;
    --backdrop-light: #c4c4c4;
    --backdrop-mid: #9a9a9a;
    --backdrop-dark: #1e1e1e;
    --accent-red: #d81f26;
    --band-red: rgba(206, 34, 40, 0.72);
    --band-red-deep: rgba(140, 0, 4, 0.85);
    --ink-dark: #1a1a1a;
    --ink-light: #ffffff;
    --brand-grey: #2e2e2e;
  }
  * { box-sizing: border-box; margin: 0; padding: 0; }
  html, body {
    width: 1200px;
    height: 1000px;
    overflow: hidden;
    background: var(--canvas-bg);
  }
  .canvas {
    position: relative;
    width: 1200px;
    height: 1000px;
  }
  .poster {
    position: absolute;
    left: 310px;
    top: 64px;
    width: 582px;
    height: 872px;
    border: 6px solid var(--poster-border);
    overflow: hidden;
    font-family: "Poiret One", "Josefin Sans", sans-serif;
  }
  .suit-photo {
    position: absolute;
    inset: 0;
    background:
      linear-gradient(90deg,
        var(--backdrop-light) 0%,
        var(--backdrop-light) 38%,
        var(--backdrop-mid) 56%,
        var(--backdrop-dark) 74%,
        var(--backdrop-dark) 100%);
  }
  .headline-top {
    position: absolute;
    top: 28px;
    left: 0;
    width: 100%;
    text-align: center;
    font-size: 36px;
    color: var(--ink-dark);
  }
  .sale-title {
    position: absolute;
    top: 124px;
    left: 0;
    width: 100%;
    text-align: center;
    font-size: 67px;
    font-weight: 400;
    line-height: 78px;
    color: var(--ink-light);
    letter-spacing: 1px;
  }
  .sale-title .red { color: var(--accent-red); }
  .discount-band {
    position: absolute;
    top: 295px;
    left: 0;
    width: 100%;
    height: 303px;
    background: linear-gradient(90deg, var(--band-red) 0%, var(--band-red) 50%, var(--band-red-deep) 78%);
  }
  .discount {
    position: absolute;
    left: 0;
    width: 100%;
    text-align: center;
    font-family: "Oswald", "Anton", sans-serif;
    font-weight: 700;
    color: var(--ink-light);
    text-shadow: -2px 2px 0 #111, -3px 3px 4px rgba(0,0,0,0.5);
    line-height: 1;
    white-space: nowrap;
  }
  .discount-low { top: 314px; font-size: 118px; }
  .discount-high { top: 449px; font-size: 123px; }
  .urgency {
    position: absolute;
    right: 18px;
    top: 618px;
    text-align: right;
    font-size: 62px;
    line-height: 63px;
    color: var(--ink-light);
    white-space: nowrap;
  }
  .brand {
    position: absolute;
    left: 14px;
    bottom: 18px;
    display: flex;
    align-items: center;
    gap: 8px;
    color: var(--brand-grey);
    font-size: 22px;
    letter-spacing: 2px;
    line-height: 1;
  }
  .brand-mark {
    width: 12px;
    height: 12px;
    background: var(--brand-grey);
  }
</style>
</head>
<body>
<div class="canvas">
  <section class="poster">
    <div class="suit-photo" role="img" aria-label="Softly blurred photo of a man in a slim-fit black suit, white shirt and dark tie, standing on the right against a light grey studio backdrop"></div>
    <p class="headline-top">Men's Suits</p>
    <h1 class="sale-title"><span class="red">CLER</span>ANCE<br><span class="red">SA</span>LE!</h1>
    <div class="discount-band"></div>
    <p class="discount discount-low">40% -</p>
    <p class="discount discount-high">60% OFF</p>
    <p class="urgency">HURRY!<br>LIMITED TIME<br>OFFER ONLY!</p>
    <p class="brand"><span class="brand-mark"></span><span class="brand-name">HARLOW MENSWEAR</span></p>
  </section>
</div>
</body>
</html>
```